Heal the world with your creativity.

We're looking for advertising materials (social media, email, etc) for a new mental health platform called PIM (www.seepim.example). PIM’s mission is to empower our members to heal and thrive by making expert advice and real-life experiences accessible to all.

Note

Facebook Cover Images: 820 x 312 pixels
LinkedIn Cover Images: 1128 x 191 pixels
3 x Social Media Post Image Templates: 1080 x 1080 pixles
3 x Enewsletter Header Image Templates: 1080 x 360 pixels
Sales One sheet: US Letter (8.5 x 11 inches)
Overview Powerpoint template: 13.33 x 7.5 inches

Fonts to Use:
Galanogrotesque
Montserrat regular

Target Market(s)

18 - 35 year olds

Industry/Entity Type

Mental Health

Requirements
Must have
• Facebook Cover Images: 820 x 312 pixels
3 x Enewsletter Header Images: 1080 x 360 pixels

Fonts to Use:
Galanogrotesque
Montserrat regular
Nice to have
• Creative copywriting for social media posts

```html
<!DOCTYPE html>
<html lang="en">
<head>
<meta charset="utf-8">
<title>PIM – Your Mental Health Made Simple</title>
<link rel="stylesheet" href="https://fonts.googleapis.com/css2?family=Poppins:wght@600;700&display=swap">
<style>
  :root {
    --navy: #124a70;
    --ring-blue: #2f86b8;
    --sky-blue: #3c93c6;
    --orange: #f47f36;
    --peach: #f6a48a;
    --white: #ffffff;
    --photo-warm: #c98a45;
    --photo-light: #e8c48e;
    --photo-shade: #6f5a3a;
  }
  html, body {
    margin: 0;
    padding: 0;
    overflow: hidden;
    background: var(--white);
  }
  .banner {
    position: relative;
    width: 1200px;
    height: 204px;
    overflow: hidden;
    background: var(--navy);
    font-family: "Poppins", sans-serif;
  }
  .banner__art {
    position: absolute;
    inset: 0;
    width: 1200px;
    height: 204px;
  }
  .brand {
    position: absolute;
    left: 53px;
    top: 29px;
    width: 126px;
    height: 126px;
    border-radius: 50%;
    background: var(--white);
    display: flex;
    align-items: center;
    justify-content: center;
    color: var(--orange);
    font-weight: 700;
    font-size: 40px;
    letter-spacing: 1px;
  }
  .headline {
    position: absolute;
    left: 560px;
    top: 27px;
    margin: 0;
    color: var(--white);
    font-weight: 700;
    text-transform: uppercase;
  }
  .headline__kicker {
    display: block;
    font-size: 23px;
    font-weight: 600;
    line-height: 28px;
    letter-spacing: 0.3px;
  }
  .headline__main {
    display: block;
    font-size: 62px;
    line-height: 64px;
    margin-top: 4px;
    letter-spacing: 0.5px;
  }
</style>
</head>
<body>
  <div class="banner">
    <svg class="banner__art" viewBox="0 0 1128 192" preserveAspectRatio="none" aria-hidden="false">
      <defs>
        <clipPath id="photo-clip">
          <circle cx="272" cy="104" r="100"/>
        </clipPath>
        <linearGradient id="photo-tones" x1="0" y1="0" x2="1" y2="1">
          <stop offset="0" stop-color="var(--photo-warm)"/>
          <stop offset="0.45" stop-color="var(--photo-light)"/>
          <stop offset="1" stop-color="var(--photo-shade)"/>
        </linearGradient>
      </defs>

      <!-- decorative rings around the portrait -->
      <circle class="ring" cx="272" cy="150" r="148" fill="none" stroke="var(--ring-blue)" stroke-width="12" opacity="0.55"/>
      <circle class="ring-fill" cx="272" cy="104" r="116" fill="var(--ring-blue)" opacity="0.35"/>

      <!-- portrait photo area -->
      <g role="img" aria-label="Photo of a young woman with shoulder-length blonde hair in a park with autumn trees">
        <rect x="160" y="0" width="230" height="192" fill="url(#photo-tones)" clip-path="url(#photo-clip)"/>
      </g>

      <!-- accent dots -->
      <circle class="accent-blue" cx="402" cy="186" r="52" fill="var(--sky-blue)" opacity="0.9"/>
      <circle class="accent-orange" cx="381" cy="96" r="13" fill="var(--orange)"/>
      <circle class="accent-white" cx="455" cy="163" r="6" fill="var(--white)"/>

      <!-- top-right bubbles -->
      <circle class="bubble-orange" cx="990" cy="8" r="108" fill="var(--orange)"/>
      <circle class="bubble-blue" cx="1060" cy="82" r="50" fill="var(--sky-blue)"/>
      <clipPath id="overlap-clip"><circle cx="990" cy="8" r="108"/></clipPath>
      <circle class="bubble-overlap" cx="1060" cy="82" r="50" fill="var(--peach)" clip-path="url(#overlap-clip)"/>
    </svg>

    <div class="brand">PIM</div>

    <h1 class="headline">
      <span class="headline__kicker">Your mental health</span>
      <span class="headline__main">Made<br>Simple.</span>
    </h1>
  </div>
</body>
</html>
```